Small Business Consulting Firm Needs Business Card Design

Need a sleek modern business card with 2 sides matching the colors of our logo. We will be placing these with a mailer we are sending out. These business cards will only ever be given to business owners. We operate helping businesses who are struggling with cash flow or finances. If the green and blue design needs to be moved to the right of "Brightpath Ledger Consulting" for aesthetic purposes that is ok. We will need an editable file if possible. We would like to include the reps name, email, website, and phone number. For now just use Owen Parrish, oparrish@brightpathledger.com, www.brightpathledger.com, and 855-219-7038.

```html
<!DOCTYPE html>
<html lang="en">
<head>
<meta charset="utf-8">
<title>Brightpath Ledger Consulting – Business Card</title>
<link rel="stylesheet" href="https://fonts.googleapis.com/css2?family=Open+Sans:wght@400;600&family=Roboto:wght@400;700&display=swap">
<style>
  :root {
    --backdrop: #e4e5e7;
    --card: #ffffff;
    --ink: #3d3d3f;
    --brand-blue: #1273c4;
    --brand-green: #5ea33a;
    --muted: #4a4a4a;
  }
  * { margin: 0; padding: 0; box-sizing: border-box; }
  html, body {
    width: 1200px; height: 900px; overflow: hidden;
    background: var(--backdrop);
  }
  .canvas { position: relative; width: 1200px; height: 900px; }

  .card {
    position: absolute;
    width: 620px; height: 354px;
    background: var(--card);
    box-shadow: 0 10px 28px rgba(0,0,0,0.12);
    overflow: hidden;
  }
  .card--front { left: 90px; top: 80px; }
  .card--back  { left: 490px; top: 466px; }

  /* Wordmark */
  .wordmark {
    font-family: "Open Sans", sans-serif;
    font-weight: 400;
    color: var(--ink);
    text-transform: uppercase;
    line-height: 1;
  }
  .wordmark__main { display: block; }
  .wordmark__sub  { display: block; }
  .wordmark__square {
    background: var(--brand-green);
  }

  .card--front .brand {
    position: absolute; left: 0; right: 0; top: 130px;
    display: flex; align-items: center; justify-content: center; gap: 22px;
  }
  .card--front .wordmark__square { width: 34px; height: 34px; }
  .card--front .wordmark__main { font-size: 40px; letter-spacing: 1px; }
  .card--front .wordmark__sub  { font-size: 20px; letter-spacing: 14px; margin-top: 12px; padding-left: 4px; }

  .card--back .brand {
    position: absolute; right: 30px; top: 34px;
    display: flex; align-items: center; gap: 12px;
  }
  .card--back .wordmark__square { width: 18px; height: 18px; }
  .card--back .wordmark__main { font-size: 19px; letter-spacing: 0.5px; }
  .card--back .wordmark__sub  { font-size: 10px; letter-spacing: 6.5px; margin-top: 6px; }

  /* Rep details */
  .rep { position: absolute; left: 78px; top: 118px; font-family: "Roboto", sans-serif; }
  .rep__name { font-size: 38px; font-weight: 700; line-height: 1; }
  .rep__first { color: var(--brand-blue); }
  .rep__last  { color: var(--brand-green); }
  .rep__role  { font-size: 17px; color: var(--muted); margin-top: 4px; padding-left: 14px; }
  .accent-bar {
    position: absolute; left: 0; top: 132px;
    width: 26px; height: 58px; background: var(--brand-blue);
  }

  .contacts {
    position: absolute; left: 290px; top: 230px;
    list-style: none; font-family: "Roboto", sans-serif;
    font-size: 17px; color: var(--ink);
  }
  .contacts::before {
    content: ""; display: block; width: 30px; height: 3px;
    background: var(--brand-green); margin-bottom: 8px;
  }
  .contacts__item { display: flex; align-items: center; gap: 12px; height: 26px; }
  .contacts__icon { width: 18px; height: 18px; flex: none; }
</style>
</head>
<body>
<main class="canvas">

  <section class="card card--front" aria-label="Card front">
    <div class="brand">
      <span class="wordmark__square"></span>
      <div class="wordmark">
        <span class="wordmark__main">Brightpath Ledger</span>
        <span class="wordmark__sub">Consulting</span>
      </div>
    </div>
  </section>

  <section class="card card--back" aria-label="Card back">
    <div class="brand">
      <span class="wordmark__square"></span>
      <div class="wordmark">
        <span class="wordmark__main">Brightpath Ledger</span>
        <span class="wordmark__sub">Consulting</span>
      </div>
    </div>

    <span class="accent-bar"></span>
    <div class="rep">
      <div class="rep__name"><span class="rep__first">Owen</span> <span class="rep__last">Parrish</span></div>
      <div class="rep__role">owners</div>
    </div>

    <ul class="contacts">
      <li class="contacts__item">
        <svg class="contacts__icon" viewBox="0 0 18 18" aria-hidden="true">
          <circle cx="9" cy="9" r="9" fill="var(--brand-blue)"/>
          <path d="M6 4.5l2 2-1 1.2c.6 1.3 1.6 2.3 2.9 2.9l1.2-1 2 2-1.3 1.4C9 12.6 5.4 9 5 5.8z" fill="#fff"/>
        </svg>
        <span>855-219-7038</span>
      </li>
      <li class="contacts__item">
        <svg class="contacts__icon" viewBox="0 0 18 18" aria-hidden="true">
          <rect x="1" y="4" width="16" height="11" fill="var(--brand-blue)"/>
          <path d="M1.5 4.5L9 10.5l7.5-6" fill="none" stroke="#fff" stroke-width="1.3"/>
        </svg>
        <span>oparrish@brightpathledger.com</span>
      </li>
      <li class="contacts__item">
        <svg class="contacts__icon" viewBox="0 0 18 18" aria-hidden="true">
          <circle cx="9" cy="9" r="8" fill="var(--brand-blue)"/>
          <ellipse cx="9" cy="9" rx="3.5" ry="8" fill="none" stroke="#fff" stroke-width="1"/>
          <path d="M1 9h16M2.5 5h13M2.5 13h13" stroke="#fff" stroke-width="1"/>
        </svg>
        <span>www.brightpathledger.com</span>
      </li>
    </ul>
  </section>

</main>
</body>
</html>
```